Computer consultant business card

Brimlo Software is a newly started computer consulting company. It's a small one-man company that provides mostly Velunix applications but also websites in collaboration with designers. I'm running this company on the side of full time university studies.

I want the final design to be clean and memorable. Be creative! :)

Some inspiration:
http://www.tavelpix.net/design/73519
http://www.tavelpix.net/design/2739566/business-card-design-by-quillbop
http://www.tavelpix.net/design/804613/business-card-design-by-lorvena-brukwaldsen

See attachment for my company logo.
Updates

I would like to thank everyone for submitting! I'll need a couple of days to review and ultimately select a design.

Target Market(s)

Non-technical entrepreneurs and small companies.

Industry/Entity Type

University

Requirements
Must have
• My company logo.
In any way, both colors from my logo.
First- and last name, e-mail and phone number.
Double-sided design.
Nice to have
• Something creative with the symbol in my logo

```html
<!DOCTYPE html>
<html lang="en">
<head>
<meta charset="utf-8">
<title>Brimlo Software – Business Card</title>
<link rel="stylesheet" href="https://fonts.googleapis.com/css2?family=Alegreya:wght@400;500;700&display=swap">
<style>
  :root {
    --brand-blue: #2279f5;
    --brand-dark: #2d2a2b;
    --stage: #2a2a2a;
    --card-light: #f4f4f4;
    --card-shade: #d9d9d9;
    --ink: #2b2b2b;
    --rule: #8f8f8f;
    --white: #ffffff;
  }
  * { box-sizing: border-box; margin: 0; padding: 0; }
  html, body {
    width: 1200px; height: 750px; overflow: hidden;
    background: var(--stage);
    font-family: "Alegreya", Georgia, serif;
  }
  .stage {
    position: relative; width: 1200px; height: 750px;
    display: flex; align-items: center; justify-content: center; gap: 50px;
  }
  .card {
    position: relative; width: 540px; height: 310px; overflow: hidden;
    box-shadow: 0 12px 30px rgba(0,0,0,.45);
  }

  /* Front side */
  .card--front {
    background: radial-gradient(circle at 78% 28%, var(--white) 0%, var(--card-light) 30%, var(--card-shade) 100%);
    color: var(--ink);
  }
  .front__brand {
    position: absolute; top: 36px; right: 48px;
    display: flex; align-items: center; gap: 12px;
  }
  .brand-dot { width: 40px; height: 40px; border-radius: 50%; background: var(--brand-blue); }
  .brand-name {
    font-weight: 700; font-size: 46px; line-height: 1; color: var(--brand-dark);
    letter-spacing: 1px;
  }
  .front__accent {
    position: absolute; top: 24px; right: 0; width: 16px; height: 66px; background: var(--brand-blue);
  }
  .person {
    position: absolute; top: 124px; left: 40px;
    border-left: 4px solid var(--brand-blue); padding-left: 12px;
  }
  .person__name { font-size: 26px; font-weight: 500; letter-spacing: .5px; line-height: 1.05; }
  .person__role { font-size: 13px; margin-left: 40px; }
  .contacts { position: absolute; left: 46px; top: 194px; width: 360px; list-style: none; }
  .contacts__item {
    display: flex; align-items: center; gap: 10px;
    font-size: 14px; line-height: 18px; padding: 3px 0 3px;
    border-bottom: 1px solid var(--rule);
  }
  .contacts__icon { width: 13px; height: 13px; flex: none; }

  /* Back side */
  .card--back { background: var(--brand-blue); }
  .back__brand {
    position: absolute; top: 88px; left: 0; right: 0;
    display: flex; align-items: center; justify-content: center; gap: 20px;
  }
  .back__brand .brand-dot { width: 74px; height: 74px; background: var(--white); }
  .back__brand .brand-name { font-size: 86px; color: var(--white); }
  .back__band {
    position: absolute; left: 0; right: 0; bottom: 0; height: 62px;
    background: var(--brand-dark); color: var(--white);
    display: flex; align-items: center; justify-content: center;
    font-size: 15px; letter-spacing: .5px;
  }
</style>
</head>
<body>
<main class="stage">
  <section class="card card--front" aria-label="Front of card">
    <div class="front__accent"></div>
    <div class="front__brand">
      <span class="brand-dot"></span>
      <span class="brand-name">brimlo</span>
    </div>
    <div class="person">
      <p class="person__name">TOMAS REYVE</p>
      <p class="person__role">General Manager</p>
    </div>
    <ul class="contacts">
      <li class="contacts__item">
        <svg class="contacts__icon" viewBox="0 0 12 12"><path d="M6 0a4 4 0 0 0-4 4c0 3 4 8 4 8s4-5 4-8a4 4 0 0 0-4-4zm0 5.5A1.5 1.5 0 1 1 6 2.5a1.5 1.5 0 0 1 0 3z" fill="var(--brand-blue)"/></svg>
        Sed est quam sagittis non porttitor auctor ac elit
      </li>
      <li class="contacts__item">
        <svg class="contacts__icon" viewBox="0 0 12 12"><rect x="3" y="0" width="6" height="12" rx="1.2" fill="var(--brand-blue)"/><rect x="4" y="2" width="4" height="6" fill="var(--white)"/></svg>
        +0412-738-905
      </li>
      <li class="contacts__item">
        <svg class="contacts__icon" viewBox="0 0 12 12"><rect x="0" y="2" width="12" height="8" fill="var(--brand-blue)"/><path d="M0 2l6 5 6-5" fill="none" stroke="var(--white)" stroke-width="1"/></svg>
        tomasreyve@quendalo.com
      </li>
      <li class="contacts__item">
        <svg class="contacts__icon" viewBox="0 0 12 12"><circle cx="6" cy="6" r="5.5" fill="var(--brand-blue)"/><path d="M.5 6h11M6 .5c-3 3-3 8 0 11M6 .5c3 3 3 8 0 11" fill="none" stroke="var(--white)" stroke-width=".8"/></svg>
        www.quendalo.com
      </li>
    </ul>
  </section>

  <section class="card card--back" aria-label="Back of card">
    <div class="back__brand">
      <span class="brand-dot"></span>
      <span class="brand-name">brimlo</span>
    </div>
    <div class="back__band">www.quendalo.com</div>
  </section>
</main>
</body>
</html>
```